Halvex Consulting

Hi,
I have my own network consulting business (just me)
and need to get a logo and business card design together,

Based in New Zealand,

Gareth Pollard
Unified Communications and Network Architect

/design engineer,
and would like this to be the basis for personal branding and company identity

Reason: I will be off site for a couple of days - so you have some more time

Business

• I have the basis for a optional logo - needs color -

```html
<!DOCTYPE html>
<html lang="en">
<head>
<meta charset="utf-8">
<title>Halvex Consulting – Business Cards</title>
<link href="https://fonts.googleapis.com/css2?family=Open+Sans:wght@300;400;600&display=swap" rel="stylesheet">
<style>
  :root{
    --stage:#1c1c1c;
    --blue-light:#62c6de;
    --blue-mid:#3a8fcc;
    --blue-deep:#3b2c9c;
    --violet:#5a4fb0;
    --accent:#2a7dc0;
    --ink:#3a3a3a;
    --paper:#fbfbfb;
    --white:#ffffff;
  }
  *{margin:0;padding:0;box-sizing:border-box}
  html,body{width:1200px;height:889px;overflow:hidden;background:var(--stage)}
  body{position:relative;font-family:"Open Sans",Arial,sans-serif}

  .card{position:absolute;width:515px;height:295px;border-radius:18px;overflow:hidden;
        box-shadow:0 4px 14px rgba(0,0,0,.55)}
  .card--front{
    background:
      radial-gradient(ellipse 60% 75% at 42% 58%, var(--blue-light) 0%, rgba(98,198,222,0) 70%),
      linear-gradient(115deg, var(--violet) 0%, var(--blue-mid) 45%, var(--blue-deep) 100%);
  }
  .card--back{background:var(--paper)}
  .front-left{left:76px;top:120px}
  .front-right{left:605px;top:120px}
  .back-left{left:78px;top:458px}
  .back-right{left:610px;top:458px}

  .front-mark{position:absolute;left:322px;top:108px;width:74px;height:74px;border-radius:50%;background:var(--white)}
  .front-brand{position:absolute;right:30px;top:240px;text-align:right;color:var(--white)}
  .card--front.front-right .front-brand{right:30px}
  .wordmark{font-weight:300;text-transform:uppercase;letter-spacing:.5px;font-size:21px;line-height:1}
  .tagline{font-size:11.5px;font-weight:400;margin-top:8px;letter-spacing:.1px}

  .soft-shade{position:absolute;left:255px;top:40px;width:300px;height:300px;
              background:radial-gradient(circle at 45% 40%, rgba(0,0,0,.07), rgba(0,0,0,0) 65%)}

  .person{position:absolute;right:24px;top:30px;text-align:right}
  .person-name{color:var(--accent);font-weight:600;font-size:18px;line-height:1.2}
  .person-role{color:var(--ink);font-size:14px;line-height:1.4}

  .back-mark{position:absolute;left:103px;top:78px;width:62px;height:62px;border-radius:50%;background:var(--accent)}
  .back-brand{position:absolute;left:25px;top:166px;color:#1a1a1a}
  .back-brand .wordmark{font-size:18px;font-weight:400}
  .back-brand .tagline{font-size:8.5px;margin-top:5px;color:var(--ink)}

  .address,.contacts{position:absolute;top:236px;font-size:12.5px;line-height:19px;color:var(--ink);font-weight:300}
  .address{left:25px}
  .contacts{left:178px}
  .label{color:var(--accent);font-weight:400}
  .web{color:var(--accent)}
  .gap{display:inline-block;width:10px}
</style>
</head>
<body>

  <section class="card card--front front-left">
    <div class="front-mark"></div>
    <div class="front-brand">
      <div class="wordmark">Halvex Consulting</div>
      <div class="tagline">Unified Communications and Network Architect</div>
    </div>
  </section>

  <section class="card card--front front-right">
    <div class="front-brand">
      <div class="wordmark">Halvex Consulting</div>
      <div class="tagline">Unified Communications and Network Architect</div>
    </div>
  </section>

  <section class="card card--back back-left">
    <div class="soft-shade"></div>
    <div class="person">
      <div class="person-name">Gareth Pollard</div>
      <div class="person-role">Design Engineer</div>
    </div>
    <div class="back-mark"></div>
    <div class="back-brand">
      <div class="wordmark">Halvex Consulting</div>
      <div class="tagline">Unified Communications and Network Architect</div>
    </div>
    <div class="address">12 Kerrow Lane<br>Wellington 6011<br>New Zealand</div>
    <div class="contacts">
      <span class="label">P.</span> 021 555 0148<span class="gap"></span><span class="label">M.</span> 021 555 0148<br>
      <span class="label">E.</span> gareth@halvexconsulting.com<br>
      www.<span class="web">halvexconsulting</span>.com
    </div>
  </section>

  <section class="card card--back back-right">
    <div class="person">
      <div class="person-name">Gareth Pollard</div>
      <div class="person-role">Design Engineer</div>
    </div>
    <div class="back-mark"></div>
    <div class="back-brand">
      <div class="wordmark">Halvex Consulting</div>
      <div class="tagline">Unified Communications and Network Architect</div>
    </div>
    <div class="address">12 Kerrow Lane<br>Wellington 6011<br>New Zealand</div>
    <div class="contacts">
      <span class="label">P.</span> 021 555 0148<span class="gap"></span><span class="label">M.</span> 021 555 0148<br>
      <span class="label">E.</span> gareth@halvexconsulting.com<br>
      www.<span class="web">halvexconsulting</span>.com
    </div>
  </section>

</body>
</html>
```